Business Card Design Project

We are an agricultural business based in Brisbane.
We design, manage and operate regional saleyards. Our logo is green/silver in colour and details of our business can be found on our website www.vodemarketyards.com.au

Just wanting a corporate design for some business cards and include name, position, contact details.

Thanks

Industry/Entity Type

Business

```html
<!DOCTYPE html>
<html lang="en">
<head>
<meta charset="utf-8">
<title>Vode Market Yards – Business Cards</title>
<link href="https://fonts.googleapis.com/css2?family=Questrial&display=swap" rel="stylesheet">
<style>
  :root {
    --canvas: #e4e4e4;
    --green: #22613a;
    --green-band: #ffffff;
    --paper: #f4f4f4;
    --ink-light: #f1f5f2;
    --ink-dark: #3a3a3a;
  }
  * { margin: 0; padding: 0; box-sizing: border-box; }
  html, body { width: 1200px; height: 1000px; overflow: hidden; }
  body {
    background: var(--canvas);
    font-family: "Questrial", "Century Gothic", sans-serif;
  }
  .card {
    position: absolute;
    left: 200px;
    width: 800px;
    height: 457px;
    overflow: hidden;
    box-shadow: 0 6px 18px rgba(0,0,0,0.18);
  }
  .card--back { top: 30px; background: var(--green); }
  .card--front { top: 513px; background: var(--green); }
  .card svg.card__bg { position: absolute; inset: 0; width: 100%; height: 100%; }

  .brand-name {
    position: absolute;
    font-size: 30px;
    letter-spacing: 2px;
    line-height: 1.1;
    text-transform: uppercase;
    text-align: center;
  }
  .card--back .brand-name { left: 470px; top: 180px; width: 300px; color: var(--ink-light); }
  .card--front .brand-name { left: 30px; top: 200px; width: 250px; color: var(--ink-dark); font-size: 26px; }

  .contact {
    position: absolute;
    left: 40px;
    bottom: 40px;
    color: var(--ink-light);
    font-size: 19px;
    line-height: 1.3;
    list-style: none;
  }
  .contact b { font-weight: 700; }

  .holder {
    position: absolute;
    right: 40px;
    top: 200px;
    text-align: right;
    color: var(--ink-light);
  }
  .holder__name { font-size: 32px; letter-spacing: 0.5px; }
  .holder__role { font-size: 18px; }
</style>
</head>
<body>

<section class="card card--back" aria-label="Card back">
  <svg class="card__bg" viewBox="0 0 800 457" aria-hidden="true">
    <g fill="var(--green-band)">
      <polygon points="0,0 80,0 80,270 110,300 110,457 0,457" opacity="0.18"/>
      <polygon points="80,0 160,0 160,270 190,300 190,457 110,457 110,300 80,270" opacity="0.15"/>
      <polygon points="160,0 240,0 240,270 270,300 270,457 190,457 190,300 160,270" opacity="0.12"/>
      <polygon points="240,0 320,0 320,270 350,300 350,457 270,457 270,300 240,270" opacity="0.08"/>
      <polygon points="320,0 400,0 400,270 430,300 430,457 350,457 350,300 320,270" opacity="0.05"/>
    </g>
  </svg>
  <p class="brand-name">Vode Market<br>Yards</p>
  <ul class="contact">
    <li>14 Saleyard Road</li>
    <li><b>e:</b> email@mail.com</li>
    <li><b>t:</b> 0790001234</li>
    <li>Brisbane - Australia</li>
  </ul>
</section>

<section class="card card--front" aria-label="Card front">
  <svg class="card__bg" viewBox="0 0 800 457" aria-hidden="true">
    <g fill="var(--green-band)">
      <polygon points="310,0 420,0 420,457 340,457 340,100 310,70" opacity="0.16"/>
      <polygon points="420,0 510,0 510,457 420,457" opacity="0.12"/>
      <polygon points="510,0 600,0 600,457 510,457" opacity="0.09"/>
      <polygon points="600,0 690,0 690,457 600,457" opacity="0.06"/>
      <polygon points="690,0 750,0 750,457 690,457" opacity="0.03"/>
    </g>
    <polygon points="0,0 310,0 310,70 340,100 340,457 0,457" fill="var(--paper)"/>
  </svg>
  <p class="brand-name">Vode Market<br>Yards</p>
  <div class="holder">
    <p class="holder__name">Nombre Apellido</p>
    <p class="holder__role">cargo portador</p>
  </div>
</section>

</body>
</html>
```